40k Ultra High Pressure Waterblasing Ad

We need 1 page flyer ad for our industry's brochure/membership directory.
We're a manufacturer & supplier for the Ultra High Pressure Waterblasting industry.
We'd like the ad to be simple and clean, highlighting some of our parts. Our dedication to our customers and affordable prices.
Some of the parts are Dorvell Brenmark Hoses, Sapphire Nozzles, Rotating Jetlance.

Our website is kestrivo.com

Requirements
Must have
• Dorvell Brenmark 40k Hose
• Sapphire Nozzles
• Rotating Jetlance
• **Update - Would like to incorporate the "iron comet logo w/ bulldog" from uploaded dorvell iron comet hose attachment. Highlighting the hose's features.
Nice to have
• Brief Bullet points or something else highlighting what we sell.
• - Pump replacement parts
• - Sapphire Nozzles
• - Rotating Jetlance
• - Fittings and adapters
• - Safety Gear
• I've uploaded past ads we've used.
Should not have
• Lots of text area

```html
<!DOCTYPE html>
<html lang="en">
<head>
<meta charset="utf-8">
<title>Kestrivo Jetting Technologies – UHP Flyer</title>
<link href="https://fonts.googleapis.com/css2?family=Montserrat:wght@700;800&family=Arimo:ital,wght@0,400;0,700;1,400&display=swap" rel="stylesheet">
<style>
  :root{
    --stage:#d9d6d6;
    --navy:#1b2f6e;
    --deep-blue:#0a4f9e;
    --mid-blue:#1478c8;
    --sky:#27a4e6;
    --pale-sky:#7fcdf3;
    --band:#0d3f86;
    --white:#ffffff;
    --ink:#1c2a55;
    --steel-light:#c9ced6;
    --steel-dark:#4a5563;
  }
  *{box-sizing:border-box;margin:0;padding:0}
  html,body{width:1200px;height:2400px;overflow:hidden;background:var(--stage)}
  .canvas{position:relative;width:1200px;height:2400px}
  .flyer{position:absolute;left:60px;top:501px;width:1080px;height:1398px;background:var(--white);overflow:hidden;box-shadow:0 20px 60px rgba(0,0,0,.25)}
  .flyer-bg{position:absolute;inset:0}
  .headline{position:absolute;top:92px;left:560px;width:500px;text-align:center;font-family:"Montserrat",sans-serif;font-weight:800;font-size:35px;line-height:1.3;color:var(--white);text-transform:uppercase;letter-spacing:.5px}
  .brand{position:absolute;left:60px;top:330px;width:440px;text-align:center;font-family:"Arimo",sans-serif;font-weight:700;color:var(--navy)}
  .brand-mark{display:flex;align-items:center;justify-content:center;gap:16px;font-size:60px;line-height:1}
  .brand-mark .dot{width:34px;height:34px;border-radius:50%;background:var(--sky)}
  .brand-name{margin-top:40px;font-size:33px;line-height:1.25}
  .offer{position:absolute;left:89px;top:694px;font-family:"Arimo",sans-serif;color:var(--navy)}
  .offer-title{font-weight:700;font-size:27px;letter-spacing:.5px;margin-bottom:18px}
  .offer-list{list-style:none}
  .offer-list li{position:relative;padding-left:36px;font-size:30px;font-weight:700;line-height:50px}
  .offer-list li::before{content:"";position:absolute;left:4px;top:15px;border-left:14px solid var(--navy);border-top:10px solid transparent;border-bottom:10px solid transparent}
  .product-photo{position:absolute;left:610px;top:400px;width:440px;height:480px;border-radius:40px;background:radial-gradient(ellipse at 50% 60%,#6d7582 0%,#3e4652 55%,rgba(62,70,82,0) 80%)}
  .tagline-band{position:absolute;left:0;top:1108px;width:1080px;height:68px;display:flex;align-items:center;justify-content:space-between;padding:0 80px 0 89px;font-family:"Arimo",sans-serif;color:var(--white);font-size:25px}
  .tagline-band .family{font-weight:700}
  .tagline-band .promise{font-style:italic}
  .footer{position:absolute;left:89px;top:1208px;right:40px;height:130px;display:flex;align-items:center;font-family:"Arimo",sans-serif}
  .origin-badge{width:133px;height:122px;background:var(--sky);border:4px solid var(--navy)}
  .partner{margin-left:30px;display:flex;align-items:center;gap:8px;font-weight:700;font-size:22px;color:var(--ink);white-space:nowrap}
  .partner .sq{width:14px;height:14px;background:var(--ink)}
  .partner-box{border:2px solid var(--steel-dark);padding:10px 12px}
  .divider{width:3px;height:110px;background:var(--ink);margin:0 22px 0 28px}
  .contact{color:var(--ink);line-height:1.28}
  .contact .email,.contact .web{font-size:27px}
  .contact .phone{font-size:37px;font-weight:700}
</style>
</head>
<body>
<div class="canvas">
  <section class="flyer">
    <svg class="flyer-bg" width="1080" height="1398" viewBox="0 0 1080 1398" aria-hidden="true">
      <defs>
        <linearGradient id="topBlue" x1="0" y1="0" x2="1" y2="1">
          <stop offset="0" stop-color="#2fb0ee"/>
          <stop offset=".55" stop-color="#1478c8"/>
          <stop offset="1" stop-color="#0a4f9e"/>
        </linearGradient>
        <linearGradient id="bottomWave" x1="0" y1="0" x2="1" y2="0">
          <stop offset="0" stop-color="#7fcdf3"/>
          <stop offset="1" stop-color="#1a8fd8"/>
        </linearGradient>
      </defs>
      <rect width="1080" height="1108" fill="url(#topBlue)"/>
      <path d="M0 120 C180 60 420 70 620 200 L620 260 C400 140 180 150 0 230 Z" fill="#0a4f9e" opacity=".55"/>
      <path d="M0 250 C200 160 430 170 600 290 C540 520 520 800 640 1000 C430 1050 200 1075 0 1108 Z" fill="var(--white)"/>
      <path d="M560 270 C700 200 900 230 1080 300 L1080 1000 C960 1060 820 1070 640 1010 C520 800 520 520 560 270 Z" fill="#0a4f9e"/>
      <path d="M600 310 C740 250 920 280 1050 340 C1080 560 1060 820 1000 960 C860 1010 760 1000 660 960 C580 760 570 520 600 310 Z" fill="#1c9ae0"/>
      <path d="M300 1108 C520 1020 780 1000 1080 960 L1080 1108 Z" fill="url(#bottomWave)"/>
      <rect y="1108" width="1080" height="68" fill="var(--band)"/>
      <rect x="560" y="1108" width="520" height="68" fill="#1f8bd6"/>
    </svg>

    <h1 class="headline">Supplying the essentials<br>in the UHP surface<br>preparation industry</h1>

    <div class="brand">
      <div class="brand-mark"><span class="dot"></span>Kestrivo</div>
      <p class="brand-name">Kestrivo Jetting<br>Technologies Inc.</p>
    </div>

    <div class="offer">
      <p class="offer-title">AT AFFORDABLE PRICES</p>
      <ul class="offer-list">
        <li>Pump replacement parts</li>
        <li>Sapphire Nozzles</li>
        <li>Rotating Jetlance</li>
        <li>Fittings and adapters</li>
        <li>Safety Gear</li>
      </ul>
    </div>

    <div class="product-photo" role="img" aria-label="Product photo: coiled grey high pressure hose with a rotating jetlance gun on top and a row of sapphire nozzles and fittings in front"></div>

    <div class="tagline-band">
      <span class="family">Family Owned and Operated</span>
      <span class="promise">“Our Customers Come First”</span>
    </div>

    <footer class="footer">
      <div class="origin-badge" role="img" aria-label="Made in USA badge"></div>
      <div class="partner"><span class="sq"></span>Dorvell</div>
      <div class="partner partner-box">Iron Comet</div>
      <div class="divider"></div>
      <div class="contact">
        <p class="email">Email: info@kestrivo.com</p>
        <p class="phone">Call: 555-014-2870</p>
        <p class="web">www.kestrivo.com</p>
      </div>
    </footer>
  </section>
</div>
</body>
</html>
```